Quill Refrigeration. Refrigeration and air conditioning specialists.

We need a website to promote our business. We would a modern simple design using the colours from our logo and black. We want it to be fun but proffesional.

Target Market(s)

Commercial

Number of Pages Required

4 page

Requirements
Must have
• Home Page, About Us, Services and Contact Us.
• 24/7 365 days service available.
• Quill Refrigeration's dedicated team specialises in commercial refrigeration and air conditioning equipment.
• Based in Joondalup, we cover Perth Metro and surrounding areas.
Nice to have
• KNOWLEDGE . EXPERIENCE . PASSION in bold.
• Our experienced and highly trained technicians provide extensive knowledge and exceptional skills for your commercial refrigeration and air conditioning requirements.
• Pictures of commercial refrigeration.
Should not have
• No mention of domestic services.

```html
<!DOCTYPE html>
<html lang="en">
<head>
<meta charset="utf-8">
<title>Quill Refrigeration</title>
<link href="https://fonts.googleapis.com/css2?family=Lato:ital,wght@0,400;0,700;0,900;1,900&family=Raleway:wght@400;500;700&display=swap" rel="stylesheet">
<style>
:root{
  --purple:#4a2a6c;
  --purple-deep:#3b1f58;
  --magenta:#a63fcf;
  --lime:#93e24c;
  --ink:#1b1b1b;
  --grey:#666;
  --line:#8a8a8a;
  --white:#fff;
}
*{box-sizing:border-box;margin:0;padding:0}
html,body{width:1200px;height:3974px;overflow:hidden}
body{position:relative;font-family:"Lato",sans-serif;color:var(--ink);background:var(--white)}
.abs{position:absolute}

/* header */
.site-header{left:0;top:0;width:1200px;height:117px;background:var(--white)}
.brand{left:92px;top:22px;font-family:"Lato",sans-serif;font-weight:900;font-size:46px;color:var(--lime);letter-spacing:1px}
.brand-sub{left:94px;top:80px;font-weight:700;font-size:13px;color:var(--purple);letter-spacing:1px}
.header-phone{left:654px;top:44px;font-weight:700;font-size:24px;color:var(--purple);display:flex;align-items:center;gap:10px}
.header-quote{left:848px;top:44px;font-weight:700;font-size:24px;color:var(--lime);display:flex;align-items:center;gap:10px}
.menu-toggle{left:1124px;top:50px;width:30px}
.menu-toggle span{display:block;height:3px;background:var(--purple);margin-bottom:5px}

/* hero */
.hero{left:0;top:117px;width:1200px;height:508px;background:linear-gradient(180deg,#2a2d36 0%,#3b3f48 55%,#1e2026 100%)}
.hero-shade{left:0;top:117px;width:1200px;height:508px;background:linear-gradient(90deg,rgba(0,0,0,.45),rgba(0,0,0,.1))}
.hero-title{left:74px;top:232px;width:620px;font-family:"Raleway",sans-serif;font-weight:500;font-size:34px;line-height:42px;color:var(--white)}
.hero-text{left:79px;top:366px;width:500px;font-weight:700;font-size:13px;line-height:21px;color:var(--white)}
.btn{display:flex;align-items:center;justify-content:center;font-family:"Lato",sans-serif;font-size:16px;font-weight:400}
.btn-call{left:79px;top:461px;width:226px;height:45px;background:var(--purple);color:var(--white)}
.btn-back{left:331px;top:461px;width:225px;height:45px;background:var(--lime);color:var(--purple-deep)}
.badge{left:1022px;top:148px}

/* about */
.section-title{font-family:"Lato",sans-serif;font-weight:700;color:var(--magenta);text-align:center}
.about-title{left:0;top:684px;width:1200px;font-size:28px}
.rule{height:2px;background:var(--magenta)}
.feature-icon{width:122px;height:122px;border-radius:50%;background:var(--purple)}
.feature-name{width:360px;text-align:center;font-weight:900;font-style:italic;font-size:24px;letter-spacing:2px}
.feature-text{width:300px;text-align:center;font-size:13px;line-height:24px;color:#333}
.range-title{left:0;top:1140px;width:1200px;font-size:26px}
.tile{width:257px;height:236px;top:1224px}
.tile-label{left:0;bottom:0;width:100%;height:59px;background:var(--purple);color:var(--white);font-weight:700;font-size:18px;line-height:21px;text-align:center;display:flex;align-items:center;justify-content:center;text-transform:uppercase;letter-spacing:.5px}

/* services */
.services{left:0;top:1534px;width:1200px;height:792px;background:var(--purple)}
.services-title{left:0;top:1586px;width:1200px;text-align:center;color:var(--white);font-weight:700;font-size:30px}
.services-rule{left:538px;top:1646px;width:124px;height:2px;background:var(--white)}
.card{width:298px;height:256px}
.card-label{position:absolute;left:0;bottom:0;width:100%;height:48px;background:rgba(255,255,255,.82);display:flex;align-items:center;justify-content:center;font-size:17px;letter-spacing:.5px;text-transform:uppercase;color:#222}
.card-open{background:var(--white);text-align:center;padding-top:46px}
.card-open h3{font-size:18px;font-weight:700;letter-spacing:.5px}
.card-open p{font-size:13px;line-height:22px;color:#444;width:240px;margin:16px auto 0}
.card-open .more{display:inline-flex;align-items:center;justify-content:center;margin-top:16px;width:138px;height:36px;background:#111;color:var(--white);font-size:14px;letter-spacing:1px}

/* clients */
.clients{left:0;top:2368px;width:1200px;height:429px;background:linear-gradient(90deg,#4d3168,#6d5886 50%,#4d3168)}
.clients-title{left:0;top:2400px;width:1200px;text-align:center;color:var(--white);font-weight:700;font-size:30px}
.clients-rule{left:470px;top:2440px;width:330px;height:2px;background:var(--white)}
.client-name{left:0;top:2474px;width:1200px;text-align:center;font-weight:900;font-size:36px;color:var(--lime);letter-spacing:2px}
.quote{left:360px;top:2558px;width:480px;text-align:center;color:var(--white);font-size:17px;line-height:26px}
.quote-mark{top:2552px;color:var(--white);font-family:"Lato",sans-serif;font-weight:900;font-size:54px;line-height:54px}
.quote-by{left:0;top:2660px;width:1200px;text-align:center;color:var(--white);font-weight:700;font-size:18px}
.dots{left:570px;top:2733px;display:flex;gap:8px}
.dots span{width:12px;height:12px;border-radius:50%;border:2px solid var(--white)}
.dots span.on{background:var(--white)}

/* contact */
.contact-name{left:0;top:2840px;width:1200px;text-align:center;font-weight:700;font-size:34px;color:var(--purple)}
.contact-sub{left:0;top:2900px;width:1200px;text-align:center;font-weight:700;font-size:27px;color:var(--ink)}
.contact-text{left:230px;top:2957px;width:740px;text-align:center;font-size:13px;line-height:22px;color:var(--grey)}
.field{border:1.5px solid #777;background:var(--white);font-size:14px;color:#333;padding:10px 8px}
.submit{left:840px;top:3428px;width:119px;height:42px;background:var(--purple);color:var(--white);font-weight:700;font-size:20px;display:flex;align-items:center;justify-content:center}

/* map + footer */
.map{left:0;top:3513px;width:1200px;height:405px;background:linear-gradient(120deg,#a9d6f5 0%,#a9d6f5 22%,#e9eee4 30%,#dfe9d6 60%,#cfe7c1 80%,#e8eee2 100%)}
.site-footer{left:0;top:3918px;width:1200px;height:56px;background:var(--purple);color:var(--white);font-size:16px}
.footer-nav{left:62px;top:19px;display:flex;gap:14px}
.footer-copy{left:0;top:19px;width:1200px;text-align:center;font-size:14px}
.footer-social{left:915px;top:16px;display:flex;align-items:center;gap:8px}
.footer-social i{display:block;width:22px;height:22px;border-radius:50%;background:#9a8bb0}
</style>
</head>
<body>

<header class="abs site-header">
  <div class="abs brand">QUILL</div>
  <div class="abs brand-sub">REFRIGERATION</div>
  <div class="abs header-phone">
    <svg width="20" height="20" viewBox="0 0 24 24"><path fill="#4a2a6c" d="M6.6 10.8a15.2 15.2 0 0 0 6.6 6.6l2.2-2.2a1 1 0 0 1 1-.25 11.4 11.4 0 0 0 3.6.57 1 1 0 0 1 1 1V20a1 1 0 0 1-1 1A17 17 0 0 1 3 4a1 1 0 0 1 1-1h3.5a1 1 0 0 1 1 1c0 1.25.2 2.45.57 3.57a1 1 0 0 1-.25 1z"/></svg>
    1300 555 019
  </div>
  <div class="abs header-quote">
    <svg width="22" height="22" viewBox="0 0 24 24" fill="none" stroke="#93e24c" stroke-width="2.4"><rect x="3" y="5" width="15" height="15" rx="1"/><path d="M9 14l1-4 9-8 3 3-9 8z"/></svg>
    Request a Quote
  </div>
  <div class="abs menu-toggle"><span></span><span></span><span></span></div>
</header>

<section>
  <div class="abs hero" role="img" aria-label="Night city skyline with lit office towers beside the water"></div>
  <div class="abs hero-shade"></div>
  <h1 class="abs hero-title">Quill Refrigeration's dedicated team specialises in commercial refrigeration and air conditioning equipment.</h1>
  <p class="abs hero-text">Lorem Ipsum is simply dummy text of the printing and typesetting industry. Lorem Ipsum has been the industry's standard dummy text ever since the 1500s</p>
  <div class="abs btn btn-call">CALL NOW</div>
  <div class="abs btn btn-back">LET US CALL YOU</div>
  <svg class="abs badge" width="128" height="128" viewBox="0 0 128 128">
    <circle cx="64" cy="64" r="50" fill="#93e24c"/>
    <path d="M64 6a58 58 0 1 1-58 58" fill="none" stroke="#93e24c" stroke-width="8"/>
    <text x="64" y="58" text-anchor="middle" font-family="Lato,sans-serif" font-weight="900" font-size="20" fill="#4a2a6c">24/7</text>
    <text x="64" y="78" text-anchor="middle" font-family="Lato,sans-serif" font-weight="700" font-size="15" fill="#fff">365 days</text>
    <text x="64" y="96" text-anchor="middle" font-family="Lato,sans-serif" font-weight="700" font-size="15" fill="#fff">service</text>
  </svg>
</section>

<section>
  <h2 class="abs section-title about-title">About Us</h2>
  <div class="abs rule" style="left:95px;top:703px;width:408px"></div>
  <div class="abs rule" style="left:676px;top:703px;width:431px"></div>

  <div class="abs feature-icon" style="left:169px;top:787px">
    <svg width="122" height="122" viewBox="0 0 122 122" fill="none" stroke="#93e24c" stroke-width="3"><path d="M38 44h20v36H38zM64 44h20v36H64zM58 50h6M42 52h12M42 60h12M68 52h12M68 60h12"/></svg>
  </div>
  <div class="abs feature-icon" style="left:538px;top:787px">
    <svg width="122" height="122" viewBox="0 0 122 122" fill="none" stroke="#93e24c" stroke-width="3"><circle cx="61" cy="52" r="12"/><path d="M56 66h10M57 72h8M38 84h46M61 32v-4M44 40l-3-3M78 40l3-3"/></svg>
  </div>
  <div class="abs feature-icon" style="left:914px;top:787px">
    <svg width="122" height="122" viewBox="0 0 122 122" fill="none" stroke="#93e24c" stroke-width="3"><path d="M61 62c-14-10-18-18-10-24 5-3 9 0 10 3 1-3 5-6 10-3 8 6 4 14-10 24zM36 80c10-6 18-6 25 0 7-6 15-6 25 0"/></svg>
  </div>

  <h3 class="abs feature-name" style="left:50px;top:940px">KNOWLEDGE</h3>
  <h3 class="abs feature-name" style="left:419px;top:940px">EXPERIENCE</h3>
  <h3 class="abs feature-name" style="left:795px;top:940px">PASSION</h3>
  <p class="abs feature-text" style="left:80px;top:995px">Lorem Ipsum is simply dummy text of the printing and typesetting industry. Lorem Ipsum has been the industry's standard dummy text ever since the 1500s</p>
  <p class="abs feature-text" style="left:449px;top:995px">Lorem Ipsum is simply dummy text of the printing and typesetting industry. Lorem Ipsum has been the industry's standard dummy text ever since the 1500s</p>
  <p class="abs feature-text" style="left:825px;top:995px">Lorem Ipsum is simply dummy text of the printing and typesetting industry. Lorem Ipsum has been the industry's standard dummy text ever since the 1500s</p>

  <h2 class="abs section-title range-title">Commercial Refrigeration</h2>
  <div class="abs tile" style="left:50px;background:linear-gradient(135deg,#6d6aa8,#b3a8d8,#7c89b8)" role="img" aria-label="Supermarket freezer aisle with glass doors">
    <div class="abs tile-label">Supermarket<br>Refrigeration</div></div>
  <div class="abs tile" style="left:334px;background:linear-gradient(135deg,#c9e69a,#eef7d6,#b7d98a)" role="img" aria-label="Empty coolroom with shelving">
    <div class="abs tile-label">Coolrooms &amp;<br>Freezer Rooms</div></div>
  <div class="abs tile" style="left:617px;background:linear-gradient(135deg,#3a2f6e,#6d5aa6,#2c2458)" role="img" aria-label="Hand touching a digital service interface">
    <div class="abs tile-label">Service &amp; Support</div></div>
  <div class="abs tile" style="left:901px;background:linear-gradient(135deg,#a9da7e,#e8f6d8,#b6e08e)" role="img" aria-label="Wall mounted air conditioning unit">
    <div class="abs tile-label">Air Conditioning</div></div>
</section>

<section>
  <div class="abs services"></div>
  <h2 class="abs services-title">Our Services</h2>
  <div class="abs services-rule"></div>

  <div class="abs card" style="left:90px;top:1701px;background:linear-gradient(135deg,#f2f2f2,#cfd4d8)" role="img" aria-label="Air conditioning unit on a white wall">
    <div class="card-label">Air Conditioning</div></div>
  <div class="abs card card-open" style="left:456px;top:1701px">
    <h3>AIR CONDITIONING</h3>
    <p>Australian summers are beautiful, and extremely hot. On the other hand, winters have been known to get quite chilly.</p>
    <span class="more">READ MORE</span>
  </div>
  <div class="abs card" style="left:821px;top:1701px;background:linear-gradient(135deg,#8fb6cf,#dfe4e6,#b9c26e)" role="img" aria-label="Drinks display fridges in a shop">
    <div class="card-label">Commercial Refrigeration</div></div>

  <div class="abs card" style="left:90px;top:1992px;background:linear-gradient(135deg,#6d87a8,#2e3f66,#9aa6b3)" role="img" aria-label="Technician servicing refrigeration equipment">
    <div class="card-label">Air Conditioning</div></div>
  <div class="abs card" style="left:456px;top:1992px;background:linear-gradient(135deg,#8d9090,#e3e6e6,#6f7373)" role="img" aria-label="Supermarket aisle of display refrigerators">
    <div class="card-label">Commercial Refrigeration</div></div>
  <div class="abs card" style="left:821px;top:1992px;background:linear-gradient(135deg,#3d6ca8,#a9c4e2,#2f5688)" role="img" aria-label="Outdoor air conditioning condenser units">
    <div class="card-label">Air Conditioning</div></div>
</section>

<section>
  <div class="abs clients" role="img" aria-label="Living room with shelves and a brick wall, tinted purple"></div>
  <h2 class="abs clients-title">Our Happy Clients</h2>
  <div class="abs clients-rule"></div>
  <div class="abs client-name">BRAMBLE</div>
  <div class="abs quote-mark" style="left:308px">&ldquo;</div>
  <p class="abs quote">Marcus and his team always provide a reliable, friendly and professional service with the job completed to a high standard.</p>
  <div class="abs quote-mark" style="left:858px">&rdquo;</div>
  <div class="abs quote-by">- Elise</div>
  <div class="abs dots"><span class="on"></span><span></span><span></span></div>
</section>

<section>
  <h2 class="abs contact-name">Quill Refrigeration</h2>
  <h3 class="abs contact-sub">Request a Quotation!</h3>
  <p class="abs contact-text">Let us provide you with a free quotation on the project you need working on. We supply quality as standard, so look no further and get in touch with Northgate Refrigeration today.</p>
  <div class="abs field" style="left:305px;top:3067px;width:323px;height:43px">Name*</div>
  <div class="abs field" style="left:638px;top:3067px;width:321px;height:43px">Company</div>
  <div class="abs field" style="left:305px;top:3142px;width:323px;height:42px">Email*</div>
  <div class="abs field" style="left:638px;top:3142px;width:321px;height:42px">Telephone*</div>
  <div class="abs field" style="left:305px;top:3213px;width:654px;height:180px">Message</div>
  <div class="abs submit">Submit</div>
</section>

<div class="abs map" role="img" aria-label="Street map of the coastal suburbs around the business location"></div>

<footer class="abs site-footer">
  <nav class="abs footer-nav"><span>Home Page</span><span>About Us</span><span>Services</span><span>Contact Us</span></nav>
  <div class="abs footer-copy">© 2018 All Right Reserved</div>
  <div class="abs footer-social"><span style="margin-right:16px">Follow Us:</span><i></i><i></i><i></i><i></i></div>
</footer>

</body>
</html>
```